Hush and Cheer Gatherings Business Card Design

I provide event planning for surprise parties, celebrating all types of life events, such as birthdays, graduations, promotions, baby showers, bridal showers, grandparent showers, health (cancer survivor), wedding anniversary etc.

I would like to see designs that show that we are fun, creative, whimical, yet professional. I am not too fond of clip art, open to all shorts of fonts and graphics, especially photos of people that appear to be saying "shh" or people being surprised.

I am open to all colors, and was considering having the same logo/business card done in different color schemes that match the occasion/client such as bright colors for a birthday, silver, gold for anniversary, pastels for a baby related party or an older person's birthday.

I would like to have the word Surprise be very bold, and stick out from the rest of the lettering..almost like people are shouting "surprise" to the honoree.

Industry/Entity Type

Event Planning

Contact Information for Business Card

Hush and Cheer Gatherings!
T Harlow President/Owner
www.hushandcheerevents.com
tharlow@hushandcheerevents.com
555 318 2947
4173 Maple Hollow Rd
Brookmere Flats PA 19099

```html
<!DOCTYPE html>
<html lang="en">
<head>
<meta charset="utf-8">
<title>Hush and Cheer Gatherings – Business Card</title>
<link rel="stylesheet" href="https://fonts.googleapis.com/css2?family=Open+Sans:wght@400;600;700;800&display=swap">
<style>
  :root {
    --page: #ffffff;
    --card: #4a2b1d;
    --card-deep: #3a2116;
    --gold: #e6ae45;
    --white: #ffffff;
    --cream: #f3e6d6;
    --photo-light: #d9c2a3;
    --photo-mid: #a9845f;
  }
  * { margin: 0; padding: 0; box-sizing: border-box; }
  html, body {
    width: 847px; height: 1200px; overflow: hidden;
    background: var(--page);
    font-family: "Open Sans", Arial, sans-serif;
  }
  .card {
    position: absolute; left: 113px; top: 93px;
    width: 587px; height: 994px;
    background: var(--card);
    border-radius: 34px; overflow: hidden;
    box-shadow: 0 2px 8px rgba(0,0,0,0.25);
    color: var(--white); text-align: center;
  }
  .brand-name {
    position: absolute; left: 0; right: 0; top: 48px;
    font-weight: 800; font-size: 62px; line-height: 1.15;
    color: var(--white);
  }
  .website {
    position: absolute; left: 0; right: 0; top: 240px;
    font-weight: 700; font-size: 30px; color: var(--gold);
  }
  .person-name {
    position: absolute; left: 0; right: 0; top: 308px;
    font-weight: 700; font-size: 36px;
  }
  .person-title {
    position: absolute; left: 0; right: 0; top: 356px;
    font-weight: 400; font-size: 26px; color: var(--cream);
  }
  .title-rule {
    position: absolute; left: 170px; width: 247px; top: 402px;
    height: 2px; background: var(--gold);
  }
  .email {
    position: absolute; left: 0; right: 0; top: 452px;
    font-size: 23px;
  }
  .address {
    position: absolute; left: 0; right: 0; top: 494px;
    font-size: 20px; line-height: 26px;
  }
  .photo {
    position: absolute; left: 0; right: 0; top: 540px; height: 354px;
    background:
      linear-gradient(to bottom, var(--card) 0%, rgba(74,43,29,0) 30%),
      radial-gradient(ellipse 55% 75% at 45% 70%, var(--photo-light) 0%, var(--photo-mid) 50%, var(--card) 100%);
  }
  .phone-bar {
    position: absolute; left: 0; right: 0; bottom: 0; height: 100px;
    background: var(--card-deep);
    display: flex; align-items: center; justify-content: center; gap: 16px;
    font-weight: 600; font-size: 40px;
  }
  .phone-icon { width: 34px; height: 34px; }
</style>
</head>
<body>
  <main class="card">
    <h1 class="brand-name">Hush and Cheer<br>Gatherings!</h1>
    <p class="website">www.hushandcheerevents.com</p>
    <p class="person-name">T Harlow</p>
    <p class="person-title">President/Owner</p>
    <div class="title-rule"></div>
    <p class="email">tharlow@hushandcheerevents.com</p>
    <p class="address">4173 Maple Hollow Rd Brookmere Flats PA 19099,<br>PO box 517</p>
    <div class="photo" role="img" aria-label="Sepia photograph of a surprised woman holding her head"></div>
    <div class="phone-bar">
      <svg class="phone-icon" viewBox="0 0 24 24" aria-hidden="true">
        <path fill="#ffffff" d="M6.6 10.8a15.1 15.1 0 0 0 6.6 6.6l2.2-2.2c.3-.3.7-.4 1-.2 1.1.4 2.3.6 3.6.6.6 0 1 .4 1 1V20c0 .6-.4 1-1 1A17 17 0 0 1 3 4c0-.6.4-1 1-1h3.5c.6 0 1 .4 1 1 0 1.3.2 2.5.6 3.6.1.3 0 .7-.2 1z"/>
      </svg>
      <span class="phone-number">555 318 2947</span>
    </div>
  </main>
</body>
</html>
```